Lena Corvell Business Card

I need a business card that reflects my current website: itslenacorvell.example and screenshot attached. If we keep the color scheme of the site and sample card below that would be ideal. The business card should include the information on the attached sample cards.

Industry/Entity Type

Business

```html
<!DOCTYPE html>
<html lang="en">
<head>
<meta charset="UTF-8">
<title>Lena Corvell Business Card</title>
<link href="https://fonts.googleapis.com/css2?family=Roboto+Condensed:wght@300&family=Caveat:wght@500&display=swap" rel="stylesheet">
<style>
  :root {
    --paper: #ffffff;
    --ink: #111111;
    --mint: #66ff99;
    --stripe: #00ff99;
    --white-text: #ffffff;
  }
  * { margin: 0; padding: 0; box-sizing: border-box; }
  html, body { width: 1200px; height: 741px; overflow: hidden; background: var(--paper); }
  .card {
    position: relative;
    width: 1200px;
    height: 741px;
    background: var(--paper);
    font-family: "Roboto Condensed", "Arial Narrow", sans-serif;
    font-weight: 300;
  }
  .card__header { position: absolute; left: 0; top: 0; width: 1200px; height: 279px; background: var(--paper); }
  .brand-name {
    position: absolute;
    left: 92px;
    top: 150px;
    font-size: 78px;
    line-height: 1;
    color: var(--ink);
    letter-spacing: 0.5px;
  }
  .card__stripe { position: absolute; left: 0; top: 279px; width: 1200px; height: 24px; background: var(--stripe); }
  .card__body { position: absolute; left: 0; top: 303px; width: 1200px; height: 438px; background: var(--mint); color: var(--white-text); }
  .tagline {
    position: absolute;
    left: 70px;
    top: 38px;
    font-family: "Caveat", cursive;
    font-size: 50px;
    line-height: 1;
    white-space: nowrap;
  }
  .tagline .star { font-family: "Roboto Condensed", sans-serif; font-size: 28px; vertical-align: 8px; margin: 0 8px; }
  .contact-line {
    position: absolute;
    left: 72px;
    top: 124px;
    font-size: 46px;
    line-height: 1;
    display: flex;
    align-items: center;
    white-space: nowrap;
  }
  .contact-line .phone-icon { width: 36px; height: 36px; margin: 0 12px 0 22px; }
  .social-line {
    position: absolute;
    left: 74px;
    top: 212px;
    height: 64px;
    display: flex;
    align-items: center;
    gap: 22px;
    font-size: 40px;
    white-space: nowrap;
  }
  .network { display: flex; align-items: center; gap: 8px; font-size: 30px; }
  .network .dot { width: 14px; height: 14px; background: var(--white-text); }
  .handle { font-size: 46px; margin-left: 6px; }
  .website {
    position: absolute;
    left: 72px;
    top: 310px;
    font-size: 50px;
    line-height: 1;
    white-space: nowrap;
  }
</style>
</head>
<body>
  <main class="card">
    <header class="card__header">
      <div class="brand-name">its Lena Corvell</div>
    </header>
    <div class="card__stripe"></div>
    <section class="card__body">
      <p class="tagline">Brand Curator<span class="star">★</span>Digital Storyteller<span class="star">★</span>Social Entrprenuer</p>
      <p class="contact-line">
        <span class="email">me@lenacorvell.example</span>
        <svg class="phone-icon" viewBox="0 0 24 24" aria-hidden="true">
          <path fill="#ffffff" d="M6.6 10.8c1.4 2.8 3.8 5.1 6.6 6.6l2.2-2.2c.3-.3.7-.4 1-.2 1.1.4 2.3.6 3.6.6.6 0 1 .4 1 1V20c0 .6-.4 1-1 1C10.6 21 3 13.4 3 4c0-.6.4-1 1-1h3.5c.6 0 1 .4 1 1 0 1.3.2 2.5.6 3.6.1.3 0 .7-.2 1l-2.3 2.2z"/>
        </svg>
        <span class="phone">240.555.0147</span>
      </p>
      <div class="social-line">
        <span class="network"><span class="dot"></span>Folio</span>
        <span class="network"><span class="dot"></span>Chirp</span>
        <span class="network"><span class="dot"></span>Lens</span>
        <span class="handle">@itslenacorvell</span>
      </div>
      <p class="website">www.itslenacorvell.example</p>
    </section>
  </main>
</body>
</html>
```